KVT Wellness Co Business Card for food and Beverage Falcons & Lanterns

One main business card design for a wellness enterprise which represents two brands. We need one primary card design, for two different employees. The only difference between the cards will be the name, title and phone number for each employee, all other design elements will be same.
I've uploaded the logos for each brand. I have also uploaded a mockup which I made using Google's drawing tool. I can provide example images of business cards we find attractive if you would like some help picturing what we like.
I'm picturing the color splash on the back of the card below the two logos to be a dark burgundy or blue. This may sound a bit silly but the feel of the card and color should look almost like wizard dress robes. Dark emerald green, dark blue and dark burgundy with black undertones and gold lace.
Updates

Reason: Thank you all for the submissions. I will need some extra time to give you feedback. Cheers

Target Market(s)

Healthy food and beverage industry

Industry/Entity Type

Health And Wellness

Contact Information for Business Card

On one side we would like the business name, location, title of employee, employee name and contact details. On the flip side we would like our two brand logos and a splash of color. We would like the card to have a black font with some gold accents if possible. We would also like the trim of the business card or a middle ply within the card stock to have a color other than white.

Font styles to use
Serif

Colors
ec1f27
0255a3
00a990

Requirements
Must have
• Bold dark colors, happy to provide sample photos of business cards I like from clipnook. Must have a version for two different employees. Must be sharp, modern and chic.
Nice to have
• Thick card stock layer in between the front and back of card that is either black or gold lace or something to make it feel, well let's say to make it feel expensive.
Should not have
• Should not have any cartoon-ey elements. All business.

```html
<!DOCTYPE html>
<html lang="en">
<head>
<meta charset="utf-8">
<title>KVT Wellness Co – Business Card</title>
<link rel="stylesheet" href="https://fonts.googleapis.com/css2?family=Source+Sans+3:wght@400;600;700&display=swap">
<style>
  :root {
    --backdrop: #3f3f3f;
    --card-black: #000000;
    --card-light: #efefef;
    --burgundy: #5e0019;
    --band-black: #0d0d0d;
    --gold: #cc9900;
    --text-light: #e6e6e6;
    --text-dark: #111111;
  }
  * { margin: 0; padding: 0; box-sizing: border-box; }
  html, body {
    width: 1200px;
    height: 900px;
    overflow: hidden;
  }
  body {
    background: var(--backdrop);
    font-family: "Source Sans 3", Arial, sans-serif;
    position: relative;
  }
  .card {
    position: absolute;
    top: 170px;
    width: 347px;
    height: 561px;
    overflow: hidden;
  }
  .card--front {
    left: 259px;
    background: var(--card-black);
    color: var(--text-light);
    text-align: center;
  }
  .card--back {
    left: 649px;
    background: var(--card-light);
  }
  .company {
    position: absolute;
    top: 58px;
    width: 100%;
  }
  .company__name {
    font-size: 23px;
    font-weight: 600;
    line-height: 1.1;
  }
  .company__location {
    font-size: 17px;
    font-weight: 400;
    margin-top: 3px;
  }
  .employee {
    position: absolute;
    top: 351px;
    width: 100%;
  }
  .employee__name {
    font-size: 23px;
    font-weight: 700;
    color: var(--gold);
    line-height: 1.1;
  }
  .employee__title {
    font-size: 15.5px;
    margin-top: 3px;
  }
  .contact {
    position: absolute;
    top: 428px;
    width: 100%;
  }
  .contact__icons {
    display: flex;
    justify-content: center;
    gap: 4px;
    margin-bottom: 6px;
  }
  .contact__icon {
    width: 22px;
    height: 22px;
    display: block;
  }
  .contact__line {
    font-size: 17.5px;
    line-height: 23px;
  }
  .brand-mark {
    position: absolute;
    left: 0;
    width: 100%;
    text-align: center;
    font-size: 22px;
    font-weight: 600;
    color: var(--text-dark);
  }
  .brand-mark--primary { top: 106px; }
  .brand-mark--secondary { top: 236px; }
  .color-splash {
    position: absolute;
    left: 0;
    top: 0;
    width: 347px;
    height: 561px;
  }
  .color-splash .band--burgundy { fill: var(--burgundy); }
  .color-splash .band--black { fill: var(--band-black); }
  .color-splash .band--gold { fill: var(--gold); }
</style>
</head>
<body>
  <section class="card card--front" aria-label="Business card front">
    <div class="company">
      <h1 class="company__name">KVT Wellness Co</h1>
      <p class="company__location">Oakmere,CA</p>
    </div>
    <div class="employee">
      <h2 class="employee__name">Marcus Ellery</h2>
      <p class="employee__title">Beverage Alchemist</p>
    </div>
    <div class="contact">
      <div class="contact__icons">
        <svg class="contact__icon" viewBox="0 0 22 22" aria-hidden="true">
          <circle cx="11" cy="11" r="11" fill="var(--gold)"/>
          <path d="M7.6 5.8c.4-.3 1-.2 1.2.2l1.1 1.9c.2.4.1.8-.2 1.1l-.7.6c.5 1.2 1.4 2.2 2.6 2.8l.6-.7c.3-.3.8-.4 1.1-.2l1.9 1.1c.4.2.5.8.2 1.2l-.8 1c-.4.5-1.1.7-1.7.5-2.9-1-5.1-3.3-6-6.2-.2-.6 0-1.3.5-1.7z" fill="#000"/>
        </svg>
        <svg class="contact__icon" viewBox="0 0 22 22" aria-hidden="true">
          <circle cx="11" cy="11" r="11" fill="var(--gold)"/>
          <rect x="5.5" y="7" width="11" height="8" rx="1" fill="#000"/>
          <path d="M5.8 7.4 11 11.3l5.2-3.9" fill="none" stroke="var(--gold)" stroke-width="1"/>
        </svg>
      </div>
      <p class="contact__line">415.555.0142</p>
      <p class="contact__line">kvtwellnessco@mailbox.com</p>
    </div>
  </section>

  <section class="card card--back" aria-label="Business card back">
    <p class="brand-mark brand-mark--primary">KVT Wellness Co</p>
    <p class="brand-mark brand-mark--secondary">Falcons &amp; Lanterns</p>
    <svg class="color-splash" viewBox="0 0 347 561" aria-hidden="true">
      <path class="band--burgundy" d="M0 443 Q210 425 347 307 L347 561 L0 561 Z"/>
      <path class="band--black" d="M0 555 Q230 525 347 445 L347 561 L0 561 Z"/>
      <path class="band--gold" d="M150 561 Q275 535 347 502 L347 561 Z"/>
    </svg>
  </section>
</body>
</html>
```